Book Cover RE-Design Project (front/back)

I have a book cover designed in the early 90's that is severely outdated and I need a complete redesign of it.

It is for a parenting book called "Raising Roots"

I'm looking for a fresh, new, clean design - not a remake of the old cover. I will attach the old cover simply as a reference for the copy/text that should be included on the front and back.

The book is about parenting for people with kids of all ages. The current design is too "child" oriented (photos and colors) and the feeling is that the book is for only parents with younger children, when in fact the book's principles are universal for young children, teenagers, and even troubled/severely troubled teenagers.

The design should communicate that the book is authoritative, and easy to implement. Authoritative as in a bestselling book/author celebrity author rather than a college professor essay. Easy to implement as in the book give you a specific plan/blueprint rather than just a bunch of psychology ideas.

There should be some kind of "orange" element in the design since it is one of 4 books in a set and the content of the books reference the other books by color (orange, blue, green, red) - but the color does not need to be the entire cover as it is currently. If the 4 books were together you would be able to easily identify which was the blue, orange, green or red book.

The current photos show "happy families" and young children, but like said above the photos of only young children exclude the books effectiveness for older children and teens. The "happy families" photos also seem to convey an "infomercial" feel that I don't like because it feels a little staged/stock and possibly unobtainable. I would like to leave the image of an ideal outcome/family to the imagination of the reader, so photos of people/families are not necessary - but photos are not out of the question.

The logo "The Family Compass" will be attached to the project files for inclusion.

The logo "Northfield Household Academy" on the current cover will NOT be included on the new cover.
Updates

Reason: This is my first project with Artisfold and I think I should have more time to interact with the designers.

Target Market(s)

Parents 30-50 who are dealing with kids (all ages - especially teens) who are defiant, lazy, and out of control.

Industry/Entity Type

College

Requirements
Must have
• 1. Some kid of "Orange" element identifying the book as the orange book in the set of (orange, red, blue, green) The actual color of the orange element can be left up to the designer.
2. The number 1 - identifying it as #1 in the set.
3. Dr. Walter Pemberly as the author
4. The bullet points on front cover (see original cover attached to project)
5. Text/copy on back cover (see original cover attached to project)

```html
<!DOCTYPE html>
<html lang="en">
<head>
<meta charset="utf-8">
<title>Raising Roots – Book Cover Set</title>
<link href="https://fonts.googleapis.com/css2?family=PT+Sans:ital,wght@0,400;0,700;1,400&display=swap" rel="stylesheet">
<style>
  :root {
    --page: #ffffff;
    --cover: #3a3424;
    --khaki: #bcb888;
    --ink: #2b2a1c;
    --light: #d9d5b4;
    --orange: #f26a10;
    --blue: #1e9ad6;
    --green: #5a8f1a;
    --red: #8a1010;
  }
  * { box-sizing: border-box; margin: 0; padding: 0; }
  html, body { width: 1200px; height: 1200px; overflow: hidden; background: var(--page); }
  body { position: relative; font-family: "PT Sans", Tahoma, sans-serif; }

  /* Publisher name */
  .brand {
    display: block; width: max-content; font-size: 13px; font-weight: 400;
    color: var(--light); letter-spacing: 0.3px; white-space: nowrap;
  }

  /* Back cover */
  .back-cover {
    position: absolute; left: 99px; top: 66px; width: 493px; height: 699px;
    background: var(--cover);
  }
  .back-panel {
    position: absolute; left: 66px; top: 105px; width: 361px; height: 487px;
    background: var(--khaki); border-top-right-radius: 32px;
    padding: 10px 25px 0;
    color: var(--ink);
  }
  .back-panel .brand { color: var(--ink); margin: 0 auto; }
  .back-heading {
    text-align: center; color: var(--orange); font-weight: 700; font-size: 14px;
    margin-top: 9px;
  }
  .back-copy { font-size: 9.6px; line-height: 12px; text-align: justify; margin-top: 18px; }
  .back-copy + .back-copy { margin-top: 12px; }
  .benefits { list-style: none; margin-top: 30px; font-size: 9.6px; line-height: 12px; }
  .benefits li { position: relative; padding-left: 14px; margin-bottom: 13px; text-align: justify; }
  .benefits li svg { position: absolute; left: 0; top: 2px; width: 9px; height: 8px; fill: var(--orange); }

  /* Front cover */
  .front-cover {
    position: absolute; width: 490px; height: 699px; background: var(--cover);
    --accent: var(--orange);
  }
  .front-cover.main { left: 610px; top: 66px; }
  .front-cover .brand { position: absolute; top: 20px; left: 50%; transform: translateX(-50%); }
  .series-number {
    position: absolute; left: 58px; top: 183px; font-size: 40px; font-weight: 700;
    color: var(--accent); line-height: 1;
  }
  .author {
    position: absolute; left: 60px; top: 230px; font-size: 14px; font-weight: 700;
    color: var(--light);
  }
  .title {
    position: absolute; left: 56px; top: 242px; font-size: 55px; font-weight: 700;
    color: var(--accent); letter-spacing: 1px; line-height: 1.05; white-space: nowrap;
  }
  .topics {
    position: absolute; right: 56px; top: 303px; list-style: none; text-align: right;
    font-style: italic; font-size: 12px; line-height: 11.5px; color: var(--light);
  }
  .heart { position: absolute; left: 229px; top: 425px; width: 34px; height: 30px; fill: var(--accent); }
  .family-art {
    position: absolute; left: 98px; top: 465px; width: 296px; height: 146px;
    background: linear-gradient(180deg, #bcb888 0%, #aba777 100%); border-radius: 4px;
  }

  /* Series thumbnails */
  .series-thumb { position: absolute; top: 805px; width: 242px; height: 345px; overflow: hidden; }
  .series-thumb .front-cover { left: 0; top: 0; transform: scale(0.494); transform-origin: 0 0; }
  .thumb-1 { left: 96px; }
  .thumb-2 { left: 350px; }
  .thumb-3 { left: 603px; }
  .thumb-4 { left: 857px; }
  .blue { --accent: var(--blue) !important; }
  .green { --accent: var(--green) !important; }
  .red { --accent: var(--red) !important; }
</style>
</head>
<body>

<svg width="0" height="0" style="position:absolute">
  <defs>
    <symbol id="heart-icon" viewBox="0 0 24 21">
      <path d="M12 21 L2.2 11.2 A6 6 0 0 1 12 3.4 A6 6 0 0 1 21.8 11.2 Z"/>
    </symbol>
  </defs>
</svg>

<section class="back-cover">
  <div class="back-panel">
    <span class="brand">The Family Compass</span>
    <h2 class="back-heading">RAISING ROOTS - Your Starting Point</h2>
    <p class="back-copy">Lorem ipsum dolor sit amet, consectetur adipisicing elit, sed do eiusmod tempor incididunt ut labore et dolore magna aliqua. Ut enim ad minim veniam, quis nostrud exercitation ullamco laboris nisi ut aliquip ex ea commodo consequat.</p>
    <p class="back-copy">Duis aute irure dolor in reprehenderit in voluptate velit esse cillum dolore eu fugiat nulla pariatur. Excepteur sint occaecat cupidatat non proident, sunt in culpa qui officia deserunt mollit anim id est laborum.</p>
    <ul class="benefits">
      <li><svg><use href="#heart-icon"/></svg>Sed ut perspiciatis unde omnis iste natus error sit voluptatem accusantium doloremque laudantium, totam rem aperiam, eaque ipsa quae ab illo inventore veritatis et quasi architecto beatae vitae dicta sunt explicabo.</li>
      <li><svg><use href="#heart-icon"/></svg>Nemo enim ipsam voluptatem quia voluptas sit aspernatur aut</li>
      <li><svg><use href="#heart-icon"/></svg>Magni dolores eos qui ratione voluptatem sequi nesciunt. Neque</li>
      <li><svg><use href="#heart-icon"/></svg>Qui dolorem ipsum quia dolor sit amet, consectetur, adipisci</li>
      <li><svg><use href="#heart-icon"/></svg>Vlit, sed quia non numquam eius modi tempora incidunt ut labore</li>
      <li><svg><use href="#heart-icon"/></svg>Et dolore magnam aliquam quaerat voluptatem. Ut enim ad</li>
      <li><svg><use href="#heart-icon"/></svg>Minima veniam, quis nostrum exercitationem ullam corporis</li>
      <li><svg><use href="#heart-icon"/></svg>Suscipit laboriosam, nisi ut aliquid ex ea commodi consequatur?</li>
    </ul>
  </div>
</section>

<section class="front-cover main">
  <span class="brand">The Family Compass</span>
  <div class="series-number">#1</div>
  <div class="author">Dr. Walter Pemberly</div>
  <h1 class="title">RAISING ROOTS</h1>
  <ul class="topics">
    <li>Behavior Modification</li>
    <li>Consequences</li>
    <li>Punishment</li>
    <li>Personality Codes</li>
  </ul>
  <svg class="heart"><use href="#heart-icon"/></svg>
  <div class="family-art" role="img" aria-label="Illustration of a family of four holding hands"></div>
</section>

<div class="series-thumb thumb-1">
  <section class="front-cover">
    <span class="brand">The Family Compass</span>
    <div class="series-number">#1</div>
    <div class="author">Dr. Walter Pemberly</div>
    <h2 class="title">RAISING ROOTS</h2>
    <ul class="topics"><li>Behavior Modification</li><li>Consequences</li><li>Punishment</li><li>Personality Codes</li></ul>
    <svg class="heart"><use href="#heart-icon"/></svg>
    <div class="family-art" role="img" aria-label="Illustration of a family of four holding hands"></div>
  </section>
</div>

<div class="series-thumb thumb-2">
  <section class="front-cover blue">
    <span class="brand">The Family Compass</span>
    <div class="series-number">#2</div>
    <div class="author">Dr. Walter Pemberly</div>
    <h2 class="title">RAISING ROOTS</h2>
    <ul class="topics"><li>Behavior Modification</li><li>Consequences</li><li>Punishment</li><li>Personality Codes</li></ul>
    <svg class="heart"><use href="#heart-icon"/></svg>
    <div class="family-art" role="img" aria-label="Illustration of a family of four holding hands"></div>
  </section>
</div>

<div class="series-thumb thumb-3">
  <section class="front-cover green">
    <span class="brand">The Family Compass</span>
    <div class="series-number">#3</div>
    <div class="author">Dr. Walter Pemberly</div>
    <h2 class="title">RAISING ROOTS</h2>
    <ul class="topics"><li>Behavior Modification</li><li>Consequences</li><li>Punishment</li><li>Personality Codes</li></ul>
    <svg class="heart"><use href="#heart-icon"/></svg>
    <div class="family-art" role="img" aria-label="Illustration of a family of four holding hands"></div>
  </section>
</div>

<div class="series-thumb thumb-4">
  <section class="front-cover red">
    <span class="brand">The Family Compass</span>
    <div class="series-number">#4</div>
    <div class="author">Dr. Walter Pemberly</div>
    <h2 class="title">RAISING ROOTS</h2>
    <ul class="topics"><li>Behavior Modification</li><li>Consequences</li><li>Punishment</li><li>Personality Codes</li></ul>
    <svg class="heart"><use href="#heart-icon"/></svg>
    <div class="family-art" role="img" aria-label="Illustration of a family of four holding hands"></div>
  </section>
</div>

</body>
</html>
```